Trade Show Banners

We would like to have a banner made to use at a Tradeshow. We provide Managed IT Services (locate at top of banner), Business VoIP (locate in middle), and Business Internet (locate at bottom). Attached is a "mock-up" and an image for the phone we would like to use. Please use your discretion for the other images. Below is the text for each section we would like included.

Title: Unleash the Power of Local IT Solutions

IT Services That Mean Business
Experience fanatical customer service with our affordable, full-service IT solutions. We’re 100% local, ensuring leading response times and personalized support—so you can focus on what you do best.

Talk More, Worry Less with Our Telephone Services
Say goodbye to overpriced equipment and hello to our free phone plan. Keep your number and enjoy unlimited local and long-distance calling. Tailor your phone system to your business needs and rest assured—our rates are always the lowest in town.

Highspeed Internet That Sets You Apart
Stay connected with blazing-fast speeds—from 1Gbps to 10Gbps, both up and down. Benefit from a static IP address and unbeatable prices, backed by 100% local support. Get the connectivity your business deserves at the best value in town.

Elevate your business with cutting-edge technology.

```html
<!DOCTYPE html>
<html lang="en">
<head>
<meta charset="utf-8">
<title>Nexora Trade Show Banner</title>
<link rel="stylesheet" href="https://fonts.googleapis.com/css2?family=Montserrat:wght@400;500;600;700;800;900&display=swap">
<style>
  :root {
    --navy: #1e2a6e;
    --cyan: #1ba6e6;
    --ink: #05070f;
    --deep: #0d1640;
    --paper: #f4f5f7;
    --stage: #e6e6e6;
    --grey: #5a5d66;
    --white: #ffffff;
  }
  * { margin: 0; padding: 0; box-sizing: border-box; }
  html, body { width: 887px; height: 1200px; overflow: hidden; background: var(--stage); }
  body { position: relative; font-family: "Montserrat", sans-serif; }
  .banner-frame {
    position: absolute; left: 0; top: 246px; width: 887px; height: 708px; overflow: hidden;
  }
  .banner {
    position: absolute; left: 0; top: 0; width: 1146px; height: 915px;
    transform: scale(0.774); transform-origin: 0 0; background: var(--paper);
  }
  .banner-shapes { position: absolute; inset: 0; }
  .brand-name {
    position: absolute; left: 72px; top: 38px;
    font-size: 96px; font-weight: 700; color: var(--navy); letter-spacing: -2px; line-height: 1;
  }
  .headline {
    position: absolute; left: 58px; top: 192px;
    font-size: 47px; font-weight: 900; color: var(--white); line-height: 1.0; text-transform: uppercase;
  }
  .headline .accent { color: var(--cyan); }
  .headline-rule { position: absolute; left: 58px; top: 298px; width: 48px; height: 4px; background: var(--white); }
  .service { position: absolute; left: 58px; width: 520px; color: var(--white); }
  .service-icon { position: absolute; left: 0; top: 0; width: 78px; height: 78px; }
  .service-text { margin-left: 99px; }
  .service-title { font-size: 20px; font-weight: 600; line-height: 1.12; margin-bottom: 8px; }
  .service-body { font-size: 11.6px; font-weight: 400; line-height: 1.13; color: #e9ecf5; }
  .service--it { top: 332px; }
  .service--it .service-icon { top: 0; }
  .service--voice { top: 430px; }
  .service--voice .service-icon { top: 0; }
  .service--net { top: 564px; }
  .service--net .service-icon { top: -6px; }
  .tagline {
    position: absolute; left: 157px; top: 670px;
    font-size: 17.5px; font-weight: 600; color: var(--cyan); text-transform: uppercase; line-height: 1.12;
  }
  .call-line {
    position: absolute; left: 58px; top: 800px;
    font-size: 38px; font-weight: 600; color: var(--navy); line-height: 1;
  }
  .call-line .accent { color: var(--cyan); }
  .call-line .number { font-weight: 900; }
  .web-line {
    position: absolute; left: 58px; top: 850px;
    font-size: 33px; font-weight: 400; color: var(--grey); letter-spacing: 5px; line-height: 1;
  }
</style>
</head>
<body>
  <div class="banner-frame">
    <div class="banner">
      <svg class="banner-shapes" viewBox="0 0 1146 915" width="1146" height="915" xmlns="http://www.w3.org/2000/svg">
        <defs>
          <linearGradient id="photoTone" x1="0" y1="0" x2="1" y2="0.3">
            <stop offset="0" stop-color="#05070f" stop-opacity="0"/>
            <stop offset="0.35" stop-color="#1d2c6b"/>
            <stop offset="0.7" stop-color="#3c4e86"/>
            <stop offset="1" stop-color="#6f7fa6"/>
          </linearGradient>
          <linearGradient id="darkBand" x1="0" y1="0" x2="1" y2="0">
            <stop offset="0" stop-color="#04060d"/>
            <stop offset="0.45" stop-color="#0c1438"/>
            <stop offset="1" stop-color="#1a2660"/>
          </linearGradient>
          <linearGradient id="phoneTone" x1="0" y1="0" x2="0" y2="1">
            <stop offset="0" stop-color="#2b2f38"/>
            <stop offset="1" stop-color="#111318"/>
          </linearGradient>
        </defs>
        <polygon points="0,767 1146,672 1146,915 0,915" fill="var(--cyan)"/>
        <polygon points="0,167 1146,78 1146,652 0,755" fill="url(#darkBand)"/>
        <polygon points="430,135 1146,78 1146,652 430,717" fill="url(#photoTone)" role="img" aria-label="Photo of two IT professionals reviewing a laptop in a server room"/>
        <polygon points="0,790 650,746 1022,915 0,915" fill="var(--paper)"/>
        <g role="img" aria-label="Product photo of a business desk phone">
          <rect x="790" y="595" width="315" height="260" rx="16" fill="url(#phoneTone)"/>
          <rect x="895" y="615" width="190" height="90" rx="6" fill="#2e5ea8"/>
          <rect x="742" y="850" width="80" height="12" rx="6" fill="#1a1c22"/>
        </g>
      </svg>

      <div class="brand-name">Nexora</div>

      <h1 class="headline">Unleash the power<br>of local <span class="accent">IT solutions</span></h1>
      <div class="headline-rule"></div>

      <section class="service service--it">
        <svg class="service-icon" viewBox="0 0 78 78" aria-hidden="true">
          <circle cx="39" cy="39" r="37" fill="none" stroke="var(--white)" stroke-width="2"/>
          <circle cx="42" cy="32" r="11" fill="none" stroke="var(--cyan)" stroke-width="3"/>
          <circle cx="42" cy="32" r="4" fill="none" stroke="var(--cyan)" stroke-width="2.5"/>
          <g stroke="var(--cyan)" stroke-width="4" stroke-linecap="round">
            <line x1="42" y1="16" x2="42" y2="19"/><line x1="42" y1="45" x2="42" y2="48"/>
            <line x1="26" y1="32" x2="29" y2="32"/><line x1="55" y1="32" x2="58" y2="32"/>
            <line x1="31" y1="21" x2="33" y2="23"/><line x1="51" y1="41" x2="53" y2="43"/>
            <line x1="53" y1="21" x2="51" y2="23"/><line x1="33" y1="41" x2="31" y2="43"/>
          </g>
          <path d="M17 50 L27 46 L42 50 L56 46 L60 50 L44 60 L25 60 Z" fill="none" stroke="var(--cyan)" stroke-width="3" stroke-linejoin="round"/>
        </svg>
        <div class="service-text">
          <h2 class="service-title">IT Services That Mean Business</h2>
          <p class="service-body">Experience fanatical customer service with our affordable, full-service IT solutions. We’re 100% local, ensuring leading response times and personalized support—so you can focus on what you do best.</p>
        </div>
      </section>

      <section class="service service--voice">
        <svg class="service-icon" viewBox="0 0 78 78" aria-hidden="true">
          <circle cx="39" cy="39" r="37" fill="none" stroke="var(--white)" stroke-width="2"/>
          <path d="M18 32 Q39 14 60 32 L56 38 L49 35 L48 30 Q39 26 30 30 L29 35 L22 38 Z" fill="none" stroke="var(--cyan)" stroke-width="3" stroke-linejoin="round"/>
          <path d="M26 58 L30 40 L48 40 L52 58 Z" fill="none" stroke="var(--cyan)" stroke-width="3" stroke-linejoin="round"/>
          <circle cx="39" cy="49" r="5" fill="var(--cyan)"/>
        </svg>
        <div class="service-text">
          <h2 class="service-title">Talk More, Worry Less with Our<br>Telephone Services</h2>
          <p class="service-body">Say goodbye to overpriced equipment and hello to our free phone plan. Keep your number and enjoy unlimited local and long-distance calling. Tailor your phone system to your business needs and rest assured—our rates are always the lowest in town.</p>
        </div>
      </section>

      <section class="service service--net">
        <svg class="service-icon" viewBox="0 0 78 78" aria-hidden="true">
          <circle cx="39" cy="39" r="37" fill="none" stroke="var(--white)" stroke-width="2"/>
          <g fill="none" stroke="var(--cyan)" stroke-width="4.5" stroke-linecap="round">
            <path d="M16 32 Q39 12 62 32"/>
            <path d="M23 40 Q39 26 55 40"/>
            <path d="M30 47 Q39 40 48 47"/>
          </g>
          <circle cx="39" cy="55" r="4.5" fill="var(--cyan)"/>
          <path d="M44 56 L58 42" stroke="var(--white)" stroke-width="3" stroke-linecap="round"/>
        </svg>
        <div class="service-text">
          <h2 class="service-title">Highspeed Internet That Sets You Apart</h2>
          <p class="service-body">Stay connected with blazing-fast speeds—from 1Gbps to 10Gbps, both up and down. Benefit from a static IP address and unbeatable prices, backed by 100% local support. Get the connectivity your business deserves at the best value in town.</p>
        </div>
      </section>

      <p class="tagline">Elevate your business with<br>cutting-edge technology</p>

      <p class="call-line">Call us <span class="accent">today :</span> <span class="number">555-014-2290</span></p>
      <p class="web-line">www.nexoralocal.com</p>
    </div>
  </div>
</body>
</html>
```